Billboard design for retail kitchen cabinet business

We have a large 7,000 square-foot showroom of beautiful kitchen cabinet displays of all different designs and price ranges. In business for over 50 years with expert designers.
Full size Norvale Media 14' X 48' billboard
Target Market(s)
Retail public on high traffic Los Angeles streets

```html
<!DOCTYPE html>
<html lang="en">
<head>
<meta charset="utf-8">
<title>Cabinet Hall Billboard</title>
<link href="https://fonts.googleapis.com/css2?family=Montserrat:wght@400;500;600;700;800&display=swap" rel="stylesheet">
<style>
  :root {
    --page-bg: #eceae6;
    --orange: #e8581c;
    --ink: #4a463d;
    --olive: #625b4a;
    --white: #ffffff;
    --panel-light: #f4f4f4;
    --photo-wall: #e9e7e3;
    --photo-wood: #5e554c;
    --photo-floor: #8f8578;
  }
  * { margin: 0; padding: 0; box-sizing: border-box; }
  html, body {
    width: 1200px; height: 1084px; overflow: hidden;
    background: var(--page-bg);
    font-family: "Montserrat", sans-serif;
  }
  .billboard {
    position: absolute; left: 30px; top: 376px;
    width: 1140px; height: 332px;
    overflow: hidden;
    background: linear-gradient(120deg, var(--panel-light) 0%, var(--white) 60%);
    box-shadow: 0 10px 24px rgba(0,0,0,0.18);
  }
  .kitchen-photo {
    position: absolute; left: 570px; top: 0;
    width: 570px; height: 332px;
    background: linear-gradient(180deg, var(--photo-wall) 0%, var(--photo-wall) 38%, var(--photo-wood) 62%, var(--photo-floor) 100%);
  }
  .shapes { position: absolute; inset: 0; }
  .headline, .tagline, .brand { position: absolute; line-height: 1; white-space: nowrap; }
  .headline-lead { left: 45px; top: 33px; font-size: 41px; font-weight: 500; color: var(--ink); letter-spacing: -0.5px; }
  .headline-lead strong { font-weight: 800; color: var(--orange); }
  .headline-size { left: 44px; top: 66px; font-size: 73px; font-weight: 800; color: var(--orange); letter-spacing: -2px; }
  .headline-unit { left: 267px; top: 93px; font-size: 22px; font-weight: 800; color: var(--orange); }
  .headline-room { left: 46px; top: 146px; font-size: 30px; font-weight: 500; color: var(--ink); letter-spacing: 6px; }
  .tagline-lead { left: 46px; top: 199px; font-size: 13px; font-weight: 500; color: var(--ink); letter-spacing: 7.4px; }
  .tagline-years { left: 45px; top: 215px; font-size: 45px; font-weight: 800; color: var(--orange); letter-spacing: -0.5px; }
  .contact {
    position: absolute; left: 45px; top: 276px; height: 56px;
    color: var(--white); display: flex; align-items: center; gap: 16px;
    line-height: 1; white-space: nowrap;
  }
  .contact-phone { font-size: 25px; font-weight: 700; letter-spacing: -0.5px; }
  .contact-divider { font-size: 20px; font-weight: 400; }
  .contact-web { font-size: 17px; font-weight: 500; }
  .brand {
    left: 570px; top: 165px; transform: translate(-50%, -50%);
    display: flex; align-items: center; gap: 8px;
    font-size: 24px; font-weight: 800; color: var(--ink);
  }
  .brand-mark { width: 16px; height: 16px; background: var(--ink); }
</style>
</head>
<body>
  <section class="billboard">
    <div class="kitchen-photo" role="img" aria-label="Photo of a modern open-plan kitchen with dark wood cabinets, a large island with bar stools and pendant lights"></div>

    <svg class="shapes" width="1140" height="332" viewBox="0 0 1140 332" aria-hidden="true">
      <polygon class="contact-band" points="0,276 516,276 570,332 0,332" fill="var(--olive)"/>
      <polygon class="badge-diamond" points="570,-10 745,165 570,340 395,165" fill="var(--white)"/>
      <polygon class="badge-outline" points="570,21 714,165 570,309 426,165" fill="none" stroke="var(--ink)" stroke-width="1"/>
      <rect class="rule-line" x="49" y="185" width="367" height="1" fill="var(--ink)"/>
      <rect class="rule-accent" x="49" y="184" width="73" height="4" fill="var(--orange)"/>
    </svg>

    <div class="headline headline-lead">WE HAVE A <strong>LARGE</strong></div>
    <div class="headline headline-size">7,000</div>
    <div class="headline headline-unit">SQUARE-FOOT</div>
    <div class="headline headline-room">SHOWROOM</div>
    <div class="tagline tagline-lead">BEAUTIFYING KITCHENS FOR</div>
    <div class="tagline tagline-years">OVER 50 YEARS</div>

    <div class="contact">
      <span class="contact-phone">(310) 555-0148</span>
      <span class="contact-divider">|</span>
      <span class="contact-web">www.cabinethall.net</span>
    </div>

    <div class="brand"><span class="brand-mark"></span>CABINET HALL</div>
  </section>
</body>
</html>
```